Web Design needed for logo design project

I am needing an interactive website for BC. Talvor Care Management is a nationwide company that combines the front desk administrative operation within Professional offices (Dental, Chiropractic, Optometry). I am needing a website designed that will provide information for potential new clients that are interested in joining our company to provide to them administrative support. I need a design for the marketing material within the folder, I will add content later. I am looking for clean crisp professional. No dancing teeth, hearts, or EKG signals please. We need it to appeal to 27-40 years old professionals. The professions are equally divided at 50/50 female to male. I already have a logo, it will be attached.
Updates

Target Market(s)

We need it to appeal to 27-40 years old professionals. The professions are equally divided at 50/50 female to male. I already have a logo, it will be attached.

Industry/Entity Type

Marketing

Requirements
Must have
• Needs to be in Word Press. It must have scalability to various screen sizes (Monitor, Phone screen, IPad, etc). Must have a customer portal capability, so professionals can access their information through a portal on the website. Have the capability to run a practice calculator or view a video requiring that it captures the visitors information so I can contact them regarding their interest in the site. Needs to have links to social media.

```html
<!DOCTYPE html>
<html lang="en">
<head>
<meta charset="utf-8">
<title>Talvor Care Management</title>
<link rel="stylesheet" href="https://fonts.googleapis.com/css2?family=Roboto+Condensed:wght@400;700&family=Roboto:wght@300;400;500&display=swap">
<style>
:root{
  --navy:#0b4a8b;
  --navy-dark:#083d75;
  --sky:#38a7dd;
  --page:#e8e8e9;
  --white:#ffffff;
  --text:#555b62;
  --rule:#d3d5d8;
  --heading:#0b4a8b;
}
*{box-sizing:border-box;margin:0;padding:0}
html,body{width:933px;height:1200px;overflow:hidden}
body{background:var(--page);font-family:'Roboto',sans-serif;color:var(--text);position:relative}
.top-bar{position:absolute;left:0;top:0;width:933px;height:86px;background:var(--white)}
.brand{position:absolute;left:78px;top:18px;display:flex;align-items:center;gap:10px}
.brand-mark{width:36px;height:36px;background:var(--navy)}
.brand-name{font-family:'Roboto Condensed',sans-serif;font-weight:700;font-size:19px;color:var(--navy);letter-spacing:1px;line-height:1.1;width:170px}
.portal-btn{position:absolute;left:586px;top:24px;width:141px;height:36px;background:var(--sky);border-bottom:3px solid #1f8dc4;color:#fff;font-family:'Roboto Condensed',sans-serif;font-size:11.5px;display:flex;align-items:center;justify-content:center;gap:6px}
.search-box{position:absolute;left:738px;top:24px;width:115px;height:34px;border:1px solid #c9cbce;font-size:9.5px;color:#444;display:flex;align-items:center;padding-left:10px;gap:6px}
.main-nav{position:absolute;left:0;top:86px;width:933px;height:35px;background:var(--navy)}
.main-nav ul{list-style:none;display:flex;position:absolute;left:80px;height:35px}
.main-nav li{height:35px;display:flex;align-items:center;justify-content:center;color:#fff;font-family:'Roboto Condensed',sans-serif;font-size:11px;border-right:1px solid #3c6da3}
.main-nav li.active{background:var(--sky)}
.hero{position:absolute;left:80px;top:121px;width:774px;height:397px;background:linear-gradient(100deg,#c9ccd0 0%,#efe9e3 30%,#dfe6ec 60%,#bcc8d3 100%);box-shadow:0 6px 10px rgba(0,0,0,.18)}
.hero-caption{position:absolute;left:36px;top:322px;font-weight:300;font-size:26px;color:#222}
.hero-arrow{position:absolute;top:181px;width:37px;height:37px;background:#000;display:flex;align-items:center;justify-content:center}
.section-title{position:absolute;font-family:'Roboto Condensed',sans-serif;font-weight:700;font-size:13.5px;color:var(--heading)}
.video-frame{position:absolute;left:82px;top:564px;width:496px;height:192px;border:3px solid #fff;background:linear-gradient(120deg,#c9c3bd 0%,#e6e2dd 45%,#8c8e92 100%)}
.play{position:absolute;left:220px;top:66px}
.intro-photo{position:absolute;left:82px;top:797px;width:238px;height:109px;background:linear-gradient(90deg,#dcd6d3 0%,#f4f6f5 50%,#6fb1ad 100%)}
.intro-text{position:absolute;left:82px;top:918px;width:240px;font-size:10.3px;line-height:16px}
.btn{position:absolute;height:21px;background:var(--sky);color:#fff;font-family:'Roboto Condensed',sans-serif;font-size:10px;display:flex;align-items:center;justify-content:center;border:1px solid #fff}
.news-list{position:absolute;left:342px;top:794px;width:238px;list-style:none}
.news-list li{display:flex;gap:12px;padding:0 0 10px;margin-bottom:9px;border-bottom:1px solid var(--rule);font-size:10.3px;line-height:16px}
.news-list li:last-child{border-bottom:none}
.news-icon{flex:0 0 21px;height:19px;background:var(--sky);display:flex;align-items:center;justify-content:center;margin-top:4px}
.info-panel{position:absolute;left:594px;top:562px;width:260px;height:450px;background:#fff;padding:8px 9px}
.info-item{display:flex;gap:12px;padding-bottom:12px;margin-bottom:10px;border-bottom:1px solid var(--rule);height:98px}
.info-item:last-child{border-bottom:none}
.info-photo{flex:0 0 84px;height:86px}
.info-item h3{font-family:'Roboto Condensed',sans-serif;font-weight:700;font-size:12.5px;color:var(--heading);margin-top:3px}
.info-item p{font-size:10px;line-height:16px;margin-top:1px;width:132px}
.read-more{font-size:10px;font-weight:500;color:#333;margin-top:3px;display:flex;align-items:center;gap:5px}
.clients-tag{position:absolute;left:80px;top:1030px;height:19px;padding:0 7px;background:var(--navy);color:#fff;font-family:'Roboto Condensed',sans-serif;font-weight:700;font-size:10.5px;display:flex;align-items:center}
.clients-rule{position:absolute;left:80px;top:1040px;width:774px;height:1px;background:#c9cbcf}
.client-row{position:absolute;left:80px;top:1064px;width:774px;height:40px;display:flex;justify-content:space-between;align-items:center}
.client{display:flex;align-items:center;gap:6px;font-family:'Roboto',sans-serif;font-weight:500;font-size:17px;color:var(--navy)}
.client-dot{width:12px;height:12px;border-radius:50%;background:var(--sky)}
.site-footer{position:absolute;left:0;top:1124px;width:933px;height:76px;background:var(--navy);color:#fff}
.follow{position:absolute;left:80px;top:17px;font-size:9.5px;font-weight:500}
.social{position:absolute;left:80px;top:38px;display:flex;gap:5px}
.social span{width:15px;height:15px;background:#3f86c9;display:block}
.footer-links{position:absolute;right:79px;top:17px;font-size:9.5px;font-weight:500;word-spacing:1px}
.copyright{position:absolute;right:79px;top:37px;font-size:9.5px;font-weight:500}
</style>
</head>
<body>
<header class="top-bar">
  <div class="brand"><span class="brand-mark"></span><span class="brand-name">TALVOR CARE MANAGEMENT</span></div>
  <div class="portal-btn">
    <svg width="12" height="10" viewBox="0 0 12 10"><circle cx="3" cy="3" r="2" fill="#fff"/><circle cx="9" cy="3" r="2" fill="#fff"/><circle cx="6" cy="4" r="2.2" fill="#fff"/><rect x="2" y="6" width="8" height="4" rx="2" fill="#fff"/></svg>
    CUSTOMER PORTAL
  </div>
  <div class="search-box">
    <svg width="9" height="9" viewBox="0 0 9 9"><circle cx="3.8" cy="3.8" r="2.8" fill="none" stroke="#333" stroke-width="1.3"/><line x1="6" y1="6" x2="8.5" y2="8.5" stroke="#333" stroke-width="1.4"/></svg>
    SEARCH
  </div>
</header>

<nav class="main-nav">
  <ul>
    <li class="active" style="width:86px">HOME</li>
    <li style="width:122px">COMPANY</li>
    <li style="width:130px">RESOURCES</li>
    <li style="width:122px">SERVICES</li>
    <li style="width:111px">NEWS</li>
    <li style="width:95px">BLOG</li>
    <li style="width:108px;border-right:none">CONTACT US</li>
  </ul>
</nav>

<section class="hero" role="img" aria-label="Smiling businesswoman in front of colleagues talking in a bright office">
  <div class="hero-arrow" style="left:0"><svg width="10" height="14" viewBox="0 0 10 14"><path d="M8 1 2 7l6 6" fill="none" stroke="#fff" stroke-width="2.5"/></svg></div>
  <div class="hero-arrow" style="right:0"><svg width="10" height="14" viewBox="0 0 10 14"><path d="M2 1l6 6-6 6" fill="none" stroke="#fff" stroke-width="2.5"/></svg></div>
  <div class="hero-caption">HEALTH Management</div>
</section>

<h2 class="section-title" style="left:81px;top:540px">PRACTISE CALCULATOR</h2>
<div class="video-frame" role="img" aria-label="Video still of a woman working with a calculator and documents at a desk">
  <svg class="play" width="54" height="54" viewBox="0 0 54 54"><circle cx="27" cy="27" r="24" fill="rgba(255,255,255,.25)" stroke="#fff" stroke-width="4"/><path d="M21 15v24l19-12z" fill="#fff"/></svg>
</div>

<h2 class="section-title" style="left:81px;top:773px">WHAT WE DO</h2>
<div class="intro-photo" role="img" aria-label="Woman with glasses holding a tablet"></div>
<p class="intro-text">Lorem Ipsum is simply dummy text of the printing and typesetting industry. Lorem Ipsum has been the industry's.</p>
<div class="btn" style="left:81px;top:975px;width:67px">READ MORE</div>

<h2 class="section-title" style="left:341px;top:773px">LATEST NEWS</h2>
<ul class="news-list">
  <li><span class="news-icon"><svg width="7" height="9" viewBox="0 0 7 9"><path d="M1 1l4 3.5L1 8" fill="none" stroke="#fff" stroke-width="2"/></svg></span><span>Lorem Ipsum is simply dummy text of the printing and typesetting industry. Lorem Ipsum has been the industry's.</span></li>
  <li><span class="news-icon"><svg width="7" height="9" viewBox="0 0 7 9"><path d="M1 1l4 3.5L1 8" fill="none" stroke="#fff" stroke-width="2"/></svg></span><span>Contrary to popular belief, Lorem Ipsum is not simply random text. It has roots in a piece of classic.</span></li>
  <li><span class="news-icon"><svg width="7" height="9" viewBox="0 0 7 9"><path d="M1 1l4 3.5L1 8" fill="none" stroke="#fff" stroke-width="2"/></svg></span><span>There are many variations of passages of Lorem Ipsum available, but the majority have suffered alteration in some form.</span></li>
</ul>
<div class="btn" style="left:513px;top:989px;width:67px">READ NEWS</div>

<h2 class="section-title" style="left:593px;top:540px">INFORMATION</h2>
<aside class="info-panel">
  <div class="info-item">
    <div class="info-photo" role="img" aria-label="Businessmen on the phone outside an office building" style="background:linear-gradient(135deg,#7fb7df,#2d3b4d)"></div>
    <div><h3>HEALTH MANAGEMENT</h3><p>It is a long established fact that a reader will be distracted.</p><div class="read-more">Read More <svg width="4" height="6" viewBox="0 0 4 6"><path d="M0 0l4 3-4 3z" fill="#333"/></svg></div></div>
  </div>
  <div class="info-item">
    <div class="info-photo" role="img" aria-label="Businessman in a suit on a phone call" style="background:linear-gradient(135deg,#8a99a8,#3b4d63)"></div>
    <div><h3>DENTAL</h3><p>It is a long established fact that a reader will be distracted.</p><div class="read-more">Read More <svg width="4" height="6" viewBox="0 0 4 6"><path d="M0 0l4 3-4 3z" fill="#333"/></svg></div></div>
  </div>
  <div class="info-item">
    <div class="info-photo" role="img" aria-label="Businesswoman talking on a phone" style="background:linear-gradient(135deg,#b9b3ad,#4a4d52)"></div>
    <div><h3>CHIROPRACTIC</h3><p>It is a long established fact that a reader will be distracted.</p><div class="read-more">Read More <svg width="4" height="6" viewBox="0 0 4 6"><path d="M0 0l4 3-4 3z" fill="#333"/></svg></div></div>
  </div>
  <div class="info-item">
    <div class="info-photo" role="img" aria-label="Hands typing on a laptop keyboard" style="background:linear-gradient(135deg,#e7e7e7,#a9abae)"></div>
    <div><h3>OPTOMETRY</h3><p>It is a long established fact that a reader will be distracted.</p><div class="read-more">Read More <svg width="4" height="6" viewBox="0 0 4 6"><path d="M0 0l4 3-4 3z" fill="#333"/></svg></div></div>
  </div>
</aside>

<div class="clients-rule"></div>
<div class="clients-tag">OUR CLIENTS</div>
<div class="client-row">
  <span class="client">Quenvar</span>
  <span class="client">Lumtrane</span>
  <span class="client"><span class="client-dot"></span>Osterpine</span>
  <span class="client">Vadrelle</span>
  <span class="client">Pemblic</span>
  <span class="client">Zorvith</span>
</div>

<footer class="site-footer">
  <div class="follow">FOLLOW US ON</div>
  <div class="social" aria-label="Social media links"><span></span><span></span><span></span></div>
  <div class="footer-links">HOME &nbsp;|&nbsp; COMPANY &nbsp;|&nbsp; RESOURCES &nbsp;|&nbsp; SERVICES &nbsp;|&nbsp; NEWS &nbsp;|&nbsp; BLOG &nbsp;|&nbsp; CONTACT US</div>
  <div class="copyright">COPYRIGHTS @ 2014 ALL RIGHTS RESERVED</div>
</footer>
</body>
</html>
```